TORVEL Business Card Design

We need a business card design for a current Plastering company now moving to building and constructing new homes.
We have been in the Plastering(rendering) business for 15yrs and have made a good name with our customers for our Top Quality of work that we provide.
We would like TORVEL to be the main attraction with an image of architectural roof tops or house design within it. Blue Yellow and Black are colours we like but are willing to see other ideas.
We would like the design to be modern and communicate quality and experience.
Industry/Entity Type
Building
Contact Information for Business Card
TORVEL Building and Plastering
PO BOX 57390 Marlowe Darwin NT 0815
PH/Fax: 08 89317725 Email: torvel@quellnet.com
Dale: 0417396248 Rosa:0409273516
ABN:58 297 130 846

```html
<!DOCTYPE html>
<html lang="en">
<head>
<meta charset="utf-8">
<title>TORVEL Building and Plastering – Business Card</title>
<link rel="stylesheet" href="https://fonts.googleapis.com/css2?family=Maven+Pro:wght@400;500&display=swap">
<style>
  :root {
    --stage: #2b2b2b;
    --card-deep: #1a6fb9;
    --card-mid: #1f7cc6;
    --card-bright: #0aa2e4;
    --circle-core: #0c67b0;
    --circle-rim: #0aa8ec;
    --band-start: #1592dc;
    --band-end: rgba(21, 146, 220, 0.35);
    --city-top: #1d78c2;
    --city-base: #1565ad;
    --ink: #f2f8ff;
  }
  * { margin: 0; padding: 0; box-sizing: border-box; }
  html, body {
    width: 892px;
    height: 1200px;
    overflow: hidden;
    background: var(--stage);
    font-family: "Maven Pro", Arial, sans-serif;
    color: var(--ink);
  }
  .card {
    position: absolute;
    overflow: hidden;
    border-radius: 20px;
  }
  .card-shapes {
    position: absolute;
    inset: 0;
    width: 100%;
    height: 100%;
  }
  .card--front { left: 58px; top: 122px; width: 764px; height: 471px; }
  .card--back  { left: 61px; top: 602px; width: 763px; height: 472px; }

  .brand-name,
  .brand-tagline {
    position: absolute;
    font-weight: 500;
    color: var(--ink);
    white-space: nowrap;
    line-height: 1;
  }
  .card--front .brand-name    { left: 64px;  top: 125px; font-size: 41px; letter-spacing: 0.5px; }
  .card--front .brand-tagline { left: 65px;  top: 161px; font-size: 14px; }
  .card--back  .brand-name    { left: 272px; top: 154px; font-size: 56px; letter-spacing: 0.5px; }
  .card--back  .brand-tagline { left: 274px; top: 207px; font-size: 19px; }

  .address {
    position: absolute;
    left: 271px;
    top: 148px;
    font-size: 19px;
    line-height: 1;
    letter-spacing: 0.6px;
    white-space: nowrap;
  }
  .contact-list {
    position: absolute;
    left: 267px;
    top: 185px;
    list-style: none;
    font-size: 20px;
    line-height: 30.5px;
    letter-spacing: 0.6px;
    white-space: nowrap;
  }
</style>
</head>
<body>

<section class="card card--front" aria-label="Business card front">
  <svg class="card-shapes" viewBox="0 0 764 471" aria-hidden="true">
    <defs>
      <linearGradient id="front-bg" x1="0" y1="0" x2="1" y2="1">
        <stop offset="0" stop-color="var(--card-mid)"/>
        <stop offset="1" stop-color="var(--card-deep)"/>
      </linearGradient>
      <radialGradient id="front-circle" cx="0.5" cy="0.5" r="0.5">
        <stop offset="0" stop-color="var(--circle-core)"/>
        <stop offset="1" stop-color="var(--circle-rim)"/>
      </radialGradient>
      <linearGradient id="address-band" x1="0" y1="0" x2="1" y2="0">
        <stop offset="0" stop-color="var(--band-start)"/>
        <stop offset="1" stop-color="var(--band-end)"/>
      </linearGradient>
      <linearGradient id="front-city" x1="0" y1="0" x2="0" y2="1">
        <stop offset="0" stop-color="var(--city-top)" stop-opacity="0"/>
        <stop offset="0.35" stop-color="var(--city-top)"/>
        <stop offset="1" stop-color="var(--city-base)"/>
      </linearGradient>
    </defs>
    <rect width="764" height="471" fill="url(#front-bg)"/>
    <rect class="address-band" x="240" y="134" width="524" height="37" fill="url(#address-band)"/>
    <circle class="brand-circle" cx="146" cy="152" r="102" fill="url(#front-circle)"/>
    <rect class="city-area" x="0" y="290" width="764" height="181" fill="url(#front-city)"
          role="img" aria-label="City skyline of office towers with lit windows"/>
  </svg>

  <div class="brand-name">TORVEL</div>
  <div class="brand-tagline">Building and Plastering</div>

  <p class="address">PO BOX 57390 Marlowe Darwin NT 0815</p>
  <ul class="contact-list">
    <li>PH/Fax: 08 89317725</li>
    <li>Email: torvel@quellnet.com</li>
    <li>Dale: 0417396248</li>
    <li>Rosa:0409273516</li>
    <li>ABN:58 297 130 846</li>
  </ul>
</section>

<section class="card card--back" aria-label="Business card back">
  <svg class="card-shapes" viewBox="0 0 763 472" aria-hidden="true">
    <defs>
      <linearGradient id="back-bg" x1="0" y1="0" x2="1" y2="1">
        <stop offset="0" stop-color="var(--card-mid)"/>
        <stop offset="1" stop-color="var(--card-deep)"/>
      </linearGradient>
      <linearGradient id="back-sweep" x1="0" y1="1" x2="1" y2="0">
        <stop offset="0" stop-color="var(--card-mid)"/>
        <stop offset="1" stop-color="var(--card-bright)"/>
      </linearGradient>
      <radialGradient id="back-circle" cx="0.5" cy="0.5" r="0.5">
        <stop offset="0" stop-color="var(--circle-core)"/>
        <stop offset="1" stop-color="var(--circle-rim)"/>
      </radialGradient>
      <linearGradient id="back-city" x1="0" y1="0" x2="0" y2="1">
        <stop offset="0" stop-color="var(--city-top)" stop-opacity="0"/>
        <stop offset="0.35" stop-color="var(--city-top)"/>
        <stop offset="1" stop-color="var(--city-base)"/>
      </linearGradient>
    </defs>
    <rect width="763" height="472" fill="url(#back-bg)"/>
    <path class="sweep" d="M0 0 H763 V70 Q330 90 40 400 L0 430 Z" fill="url(#back-sweep)" opacity="0.55"/>
    <circle class="brand-circle" cx="381" cy="188" r="134" fill="url(#back-circle)"/>
    <rect class="city-area" x="0" y="305" width="763" height="167" fill="url(#back-city)"
          role="img" aria-label="City skyline of office towers with lit windows"/>
  </svg>

  <div class="brand-name">TORVEL</div>
  <div class="brand-tagline">Building and Plastering</div>
</section>

</body>
</html>
```